Velvane Detailing – Premium Automotive Detailing Studio Website Design

We're launching a premium automotive detailing studio called Velvane Detailing, and we’re looking for a clean, minimal, and high-end website design (desktop + mobile version). The studio targets owners of luxury vehicles who care deeply about aesthetics, perfection, and exceptional service.
This project is about more than just showing services , it should feel like a luxury experience from the very first second. The design should be modern, minimalistic, elegant, and clearly aimed at an upscale market.
We’re looking for a designer who can translate our physical studio’s premium interior and architectural feel into a digital presence.
What we want the website to feel like:
Clean and modern
Professional and luxurious
Minimal and not cluttered
Light animations or transitions to add polish
Stylish and cinematic
Design freedom:
We trust your design direction. We are not providing strict color codes or layout instructions, we want you to create what you believe works best based on our brand positioning and target audience. Just keep it premium, modern, and well-organized.
What the website should include:
Hero section with a bold visual (image or video)
About the Studio — a few blocks explaining our story and focus on quality
Service Overview — clearly showing what we offer (detailing, ceramic coating, interior, etc.)
Gallery/Showcase — show off our work with cars, interior, and the space itself
Client Lounge Area — mention comfort, coffee, and waiting space
Testimonials — social proof from satisfied clients
Location & contact section — map, address, contact form
Footer, simple with nav, contact info, and optional social media
Target audience:
Owners of high-end vehicles (Corvanti, Haldane, etc.)
Car collectors and detailing enthusiasts
People looking for premium-level service and presentation
Brands/creators booking our photo studio

```html
<!DOCTYPE html>
<html lang="en">
<head>
<meta charset="utf-8">
<title>Velvane Detailing – Premium Car Detailing Studio</title>
<link rel="stylesheet" href="https://fonts.googleapis.com/css2?family=Krona+One&family=Poppins:ital,wght@0,400;0,500;0,600;0,700;1,500&display=swap">
<style>
:root{
  --red:#d7102f;
  --red-dark:#a50b22;
  --ink:#121214;
  --night:#17171a;
  --panel:#1f1f23;
  --white:#ffffff;
  --grey:#9a9aa0;
  --line:#d9d9dd;
  --paper:#f3f3f5;
  --head:"Krona One", sans-serif;
  --body:"Poppins", sans-serif;
}
*{box-sizing:border-box;margin:0;padding:0}
html,body{width:1200px;height:5396px;overflow:hidden}
body{position:relative;font-family:var(--body);color:var(--white);background:var(--ink)}
.abs{position:absolute}
.btn{position:absolute;display:flex;align-items:center;justify-content:center;background:var(--red);color:var(--white);border-radius:22px;font:700 14px var(--body);letter-spacing:.3px;white-space:nowrap}
.heading{font-family:var(--head);text-transform:uppercase;line-height:1.1}
.heading .accent{color:var(--red);text-shadow:0 0 10px rgba(215,16,47,.7)}
.eyebrow{font:600 22px var(--body);text-transform:uppercase;color:var(--grey);text-align:center;width:100%}
.center{left:0;width:1200px;text-align:center}

/* hero */
.hero{position:absolute;left:0;top:0;width:1200px;height:1204px;background:linear-gradient(#0e0e10 0%,#1a1a1d 60%,#121214 100%)}
.hero-photo{position:absolute;left:0;top:0;width:1200px;height:760px;background:radial-gradient(ellipse at 62% 48%,#b0102a 0%,#5a1420 22%,#2c2c30 48%,#141416 80%)}
.brand{position:absolute;left:63px;top:38px;display:flex;align-items:center;gap:10px;font:700 24px var(--body);letter-spacing:1px;text-transform:uppercase}
.brand i{width:34px;height:34px;border:3px solid var(--white);display:block}
.nav{position:absolute;top:50px;left:0;font:600 13px var(--body);text-transform:uppercase}
.nav span{position:absolute;white-space:nowrap}
.hero-title{left:128px;top:203px;font-size:29px}
.about-title{left:128px;top:790px;font-size:42px}
.about-text{left:128px;top:906px;width:520px;font-size:15px;line-height:26px;color:#e8e8ea}
.about-mark{left:712px;top:880px;width:360px;text-align:center;font:700 46px var(--body);color:#c9c9cf;text-transform:uppercase;letter-spacing:2px}

/* services */
.services{position:absolute;left:0;top:1204px;width:1200px;height:777px;background:var(--white);color:var(--ink)}
.card{position:absolute;top:212px;width:299px;height:391px;border:1px solid var(--line);text-align:center}
.card .ph{height:168px}
.card h3{margin-top:24px;font:600 21px var(--body);text-transform:uppercase}
.card p{margin:18px auto 0;width:250px;font-size:14px;line-height:19px;color:#333}
.card b{position:absolute;left:0;right:0;bottom:20px;font:700 14px var(--body)}
.card b:before{content:"";position:absolute;left:95px;right:95px;top:-14px;border-top:1px solid var(--line)}

/* gallery */
.gallery{position:absolute;left:0;top:1981px;width:1200px;height:758px;background:var(--night)}
.shot{position:absolute;top:220px;height:358px}
.dots{position:absolute;top:642px;left:0;width:1200px;display:flex;justify-content:center;gap:8px}
.dots i{width:7px;height:7px;border-radius:50%;background:#777}
.dots i:first-child{background:var(--white)}

/* lounge */
.lounge{position:absolute;left:0;top:2739px;width:1200px;height:580px;background:radial-gradient(ellipse at 30% 80%,#7a1020 0%,#3b1a22 40%,#26262b 80%)}
.perk{position:absolute;top:180px;width:297px;height:285px;border:1px solid rgba(255,255,255,.55);text-align:center;background:rgba(40,40,46,.35)}
.perk svg{margin-top:34px}
.perk h3{margin-top:22px;font:600 21px var(--body);text-transform:uppercase}
.perk p{margin:10px auto 0;width:230px;font-size:15px;line-height:22px;color:#ddd}

/* testimonials */
.testimonials{position:absolute;left:0;top:3319px;width:1200px;height:566px;background:repeating-linear-gradient(135deg,#1c1c20 0 3px,#202024 3px 6px)}
.quote{position:absolute;top:283px;width:360px}
.quote .avatar{position:absolute;left-:0;left:-74px;top:0;width:52px;height:52px;border-radius:50%;background:linear-gradient(#8f97a6,#4b5260)}
.quote p{font:italic 500 14px var(--body);line-height:27px}
.quote b{display:block;margin-top:14px;font:700 13px var(--body);text-transform:uppercase}
.quote .mark{position:absolute;right:-12px;top:120px;font:700 58px/1 var(--head);color:var(--red)}

/* contact */
.contact{position:absolute;left:0;top:3885px;width:1200px;height:680px;background:var(--ink)}
.info{position:absolute;left:126px;display:flex;align-items:flex-start;gap:20px;font-size:15px;line-height:21px;color:#ddd}
.info i{flex:none;width:32px;height:32px;border-radius:50%;background:var(--red);display:flex;align-items:center;justify-content:center}
.form{position:absolute;left:586px;top:131px;width:486px;height:449px;background:var(--red)}
.form h3{text-align:center;margin-top:26px;font:700 23px var(--body);text-transform:uppercase}
.field{position:absolute;left:38px;width:410px;height:44px;background:var(--white);color:#333;font-size:14px;padding:10px 12px}

/* map */
.map-band{position:absolute;left:0;top:4793px;width:1200px;height:6px;border-top:2px solid var(--red);border-bottom:2px solid var(--red)}
.map{position:absolute;left:126px;top:4565px;width:946px;height:408px;background:linear-gradient(135deg,#ecebe6,#e3e0d8 50%,#efece4);border:1px solid #ccc}
.map-pin{position:absolute;left:460px;top:160px;width:96px;height:96px;border-radius:50%;background:var(--red);border:5px solid #fff}

/* footer */
.footer{position:absolute;left:0;top:4973px;width:1200px;height:423px;background:linear-gradient(180deg,#fafafb,#e9e9ec);color:var(--ink)}
.footer h4{position:absolute;top:62px;font:700 19px var(--body);text-transform:uppercase}
.divider{position:absolute;top:63px;width:1px;height:251px;background:#c8c8cc}
.f-item{position:absolute;left:471px;display:flex;gap:20px;font-size:15px;line-height:22px;color:#333}
.f-item i{flex:none;width:32px;height:32px;border-radius:50%;background:var(--red);display:flex;align-items:center;justify-content:center}
.links{position:absolute;left:886px;top:116px;font-size:15px;line-height:30.4px;color:#333;list-style:none}
.social{position:absolute;left:126px;top:258px;display:flex;gap:10px}
.social i{width:36px;height:36px;border-radius:50%;background:var(--ink);display:block}
</style>
</head>
<body>

<header class="hero">
  <div class="hero-photo" role="img" aria-label="Detailer pressure-washing a foam-covered red sports car in a dark studio"></div>
  <div class="brand"><i></i>Velvane</div>
  <nav class="nav">
    <span style="left:334px">Home</span>
    <span style="left:424px">About</span>
    <span style="left:520px">Services</span>
    <span style="left:635px">Gallery</span>
    <span style="left:740px">Testimonials</span>
    <span style="left:890px">Contact</span>
  </nav>
  <a class="btn" style="left:990px;top:36px;width:145px;height:44px">BOOK A SLOT</a>
  <h1 class="heading abs hero-title">Premium Car<br>Detailing Studio</h1>
  <a class="btn" style="left:128px;top:295px;width:146px;height:42px">BOOK A SLOT</a>
  <a class="btn" style="left:838px;top:220px;width:232px;height:52px;border-radius:26px;font-size:17px">CALL:VEL-555-0193</a>

  <h2 class="heading abs about-title">About<br><span class="accent">The Studio</span></h2>
  <p class="abs about-text">Lorem ipsum dolor sit amet, consectetur adipiscing elit, sed do eiusmod tempor incididunt ut labore et dolore magna aliqua. Quis ipsum suspendisse ultrices gravida. Risus commodo viv erra maecenas accumsan lacus vel facilisis.</p>
  <a class="btn" style="left:128px;top:1036px;width:146px;height:42px">READ MORE</a>
  <div class="abs about-mark">Velvane</div>
</header>

<section class="services">
  <p class="eyebrow abs" style="top:92px;color:#444">Service Overview</p>
  <h2 class="heading abs center" style="top:128px;font-size:42px">What <span class="accent">We Offer</span></h2>
  <svg class="abs" style="left:62px;top:288px" width="30" height="16" viewBox="0 0 30 16"><path d="M29 8H2M9 1 2 8l7 7" fill="none" stroke="#111" stroke-width="2"/></svg>
  <svg class="abs" style="left:1103px;top:288px" width="30" height="16" viewBox="0 0 30 16"><path d="M1 8h27M21 1l7 7-7 7" fill="none" stroke="#111" stroke-width="2"/></svg>
  <article class="card" style="left:126px"><div class="ph" role="img" aria-label="Hands polishing a black car" style="background:linear-gradient(135deg,#4a4a4e,#1e1e22 60%,#8a3a2a)"></div><h3>Detailing</h3><p>Lorem ipsum dolor sit amecons ectetur adipiscing elit, sed do eiu smod tempor incididunt ut lab ore et dolore magna alua.</p><b>READ MORE</b></article>
  <article class="card" style="left:450px"><div class="ph" role="img" aria-label="Red car being foam-washed" style="background:linear-gradient(135deg,#2a2a2e,#8a1020 55%,#1a1a1c)"></div><h3>Ceramic Coating</h3><p>Lorem ipsum dolor sit amecons ectetur adipiscing elit, sed do eiu smod tempor incididunt ut lab ore et dolore magna alua.</p><b>READ MORE</b></article>
  <article class="card" style="left:773px"><div class="ph" role="img" aria-label="Car interior dashboard being cleaned" style="background:linear-gradient(135deg,#3a4650,#1d2228 60%,#2e4a3a)"></div><h3>Interior</h3><p>Lorem ipsum dolor sit amecons ectetur adipiscing elit, sed do eiu smod tempor incididunt ut lab ore et dolore magna alua.</p><b>READ MORE</b></article>
  <a class="btn" style="left:498px;top:653px;width:202px;height:44px">VIEW ALL SERVICES</a>
</section>

<section class="gallery">
  <p class="eyebrow abs" style="top:82px">Gallery/Showcase</p>
  <h2 class="heading abs center" style="top:118px;font-size:40px">Our <span class="accent">Works</span></h2>
  <div class="shot" role="img" aria-label="Polishing machine on a black car bonnet" style="left:31px;width:382px;background:linear-gradient(135deg,#3c3c40,#151517 55%,#6a6a3a)"></div>
  <div class="shot" role="img" aria-label="Black luxury car covered in water droplets" style="left:436px;width:383px;background:linear-gradient(135deg,#5a6068,#1e2126 55%,#3a4048)"></div>
  <div class="shot" role="img" aria-label="Yellow polishing pad on a car panel in warm light" style="left:842px;width:358px;background:linear-gradient(135deg,#a86a2a,#3a2a1e 60%,#181818)"></div>
  <div class="dots"><i></i><i></i><i></i><i></i><i></i><i></i><i></i><i></i></div>
</section>

<section class="lounge" role="img" aria-label="Blurred red car in the background">
  <h2 class="heading abs center" style="top:62px;font-size:40px">Client <span class="accent">Lounge Area</span></h2>
  <div class="perk" style="left:126px">
    <svg width="84" height="80" viewBox="0 0 84 80" fill="none" stroke="#fff" stroke-width="2"><path d="M20 70C30 40 50 20 74 6 70 34 56 56 26 62M10 78l20-28M34 48l10-4M42 38l12-4M50 28l12-4"/></svg>
    <h3>Comfort</h3><p>Lorem ipsum dolor sit amet consectetur adipiscing.</p></div>
  <div class="perk" style="left:450px">
    <svg width="92" height="80" viewBox="0 0 92 80" fill="none" stroke="#fff" stroke-width="2"><path d="M34 4c-4 6 4 10 0 16M46 4c-4 6 4 10 0 16M58 4c-4 6 4 10 0 16M18 34h56c0 18-10 30-28 30S18 52 18 34ZM74 38h6a8 8 0 0 1 0 16h-10M10 70h72"/></svg>
    <h3>Coffee</h3><p>Lorem ipsum dolor sit amet consectetur adipiscing.</p></div>
  <div class="perk" style="left:777px">
    <svg width="84" height="80" viewBox="0 0 84 80" fill="none" stroke="#fff" stroke-width="2"><path d="M22 40V12a8 8 0 0 1 8-8h24a8 8 0 0 1 8 8v28M10 36a6 6 0 0 1 12 0v14h40V36a6 6 0 0 1 12 0v26H10ZM18 62v10M66 62v10"/></svg>
    <h3>Waiting Space</h3><p>Lorem ipsum dolor sit amet consectetur adipiscing.</p></div>
</section>

<section class="testimonials">
  <p class="eyebrow abs" style="top:95px">Testimonials</p>
  <h2 class="heading abs center" style="top:133px;font-size:40px">Satisfied <span class="accent">Clients</span></h2>
  <div class="quote" style="left:201px"><span class="avatar" role="img" aria-label="Client portrait"></span><p>Lorem ipsum dolor sit amet, conctetur adipi scing elit, sed do eiusmod tmpor incididunt ut labore et dolore magna aliquauis ipsumsusp endisse ultrices gravida.us commvram.</p><b>-Dara Quillen</b><span class="mark">"</span></div>
  <div class="quote" style="left:724px"><span class="avatar" role="img" aria-label="Client portrait"></span><p>Lorem ipsum dolor sit amet, conctetur adipi scing elit, sed do eiusmod tmpor incididunt ut labore et dolore magna aliquauis ipsumsusp endisse ultrices gravida.us commvram.</p><b>-Dara Quillen</b><span class="mark">"</span></div>
</section>

<section class="contact">
  <p class="abs" style="left:126px;top:166px;font:600 22px var(--body);color:var(--grey);text-transform:uppercase">Contact Us</p>
  <h2 class="heading abs" style="left:126px;top:206px;font-size:40px">Let's <span class="accent">Talk</span></h2>
  <p class="abs" style="left:126px;top:270px;width:420px;font-size:14px;line-height:20px;color:#ddd">Lorem ipsum dolor sit amecons ectetur adipiscing elit, sed do eiu smod tempor incididunt ut lab ore et dolore magna aluagravida. Risus commodo viverra maece nas accumsan lacus vel facilisis.</p>
  <div class="info" style="top:385px"><i><svg width="14" height="18" viewBox="0 0 14 18"><path d="M7 1a6 6 0 0 0-6 6c0 5 6 10 6 10s6-5 6-10a6 6 0 0 0-6-6Z" fill="none" stroke="#fff" stroke-width="1.6"/><circle cx="7" cy="7" r="2" fill="#fff"/></svg></i><span>1825 Placeholder Lane,<br>Marrowfield, KY, 40118</span></div>
  <div class="info" style="top:452px"><i><svg width="16" height="16" viewBox="0 0 16 16"><path d="M3 1l3 3-2 2c1 3 3 5 6 6l2-2 3 3-2 2C7 15 1 9 1 3Z" fill="none" stroke="#fff" stroke-width="1.5"/></svg></i><span>hello@velvanedetailing.com</span></div>
  <div class="info" style="top:502px"><i><svg width="16" height="12" viewBox="0 0 16 12"><rect x="1" y="1" width="14" height="10" fill="none" stroke="#fff" stroke-width="1.5"/><path d="M1 1l7 6 7-6" fill="none" stroke="#fff" stroke-width="1.5"/></svg></i><span>230-555-0148</span></div>
  <form class="form">
    <h3>Get In Touch</h3>
    <div class="field" style="top:80px">Name:</div>
    <div class="field" style="top:143px">Email:</div>
    <div class="field" style="top:206px">Phone:</div>
    <div class="field" style="top:268px;height:118px">Message:</div>
    <a class="btn" style="left:153px;top:367px;width:180px;height:48px;border-radius:24px;background:var(--ink);font-size:16px">SUBMIT NOW</a>
  </form>
</section>

<div class="map-band"></div>
<div class="map" role="img" aria-label="Street map showing the studio location">
  <div class="map-pin"></div>
</div>

<footer class="footer">
  <div class="abs" style="left:126px;top:150px;font:700 30px var(--body);text-transform:uppercase;letter-spacing:1px">Velvane</div>
  <div class="social"><i aria-label="Social link"></i><i aria-label="Social link"></i><i aria-label="Social link"></i><i aria-label="Social link"></i></div>
  <span class="divider" style="left:383px"></span>
  <span class="divider" style="left:806px"></span>
  <h4 style="left:471px">Contact</h4>
  <div class="f-item" style="top:116px"><i></i><span>1825 Placeholder Lane,<br>Marrowfield, KY, 40118</span></div>
  <div class="f-item" style="top:180px"><i></i><span style="line-height:32px">hello@velvanedetailing.com</span></div>
  <div class="f-item" style="top:232px"><i></i><span>000-555-0172<br>293 555 0190</span></div>
  <h4 style="left:886px">Links</h4>
  <ul class="links"><li>About the Studio</li><li>Service Overview</li><li>Gallery/Showcase</li><li>Client Lounge Area</li><li>Testimonials</li><li>Location &amp; contact</li></ul>
  <p class="abs center" style="top:350px;font-size:14px;color:#333">© 2025 Velvane Detailing &nbsp;All rights reserved.</p>
</footer>

</body>
</html>
```